Real estate agent : RT Estates

I have done the attached logo designed by your company .
My business card description as below:
Name : Daniel Brooks
Mobile: 0412583047
Email : danielb@rtestates-demo.net.au
Sales & Property Management

```html
<!DOCTYPE html>
<html lang="en">
<head>
<meta charset="utf-8">
<title>RT Estates – Business Card</title>
<link rel="stylesheet" href="https://fonts.googleapis.com/css2?family=Montserrat:wght@700;800&family=Arimo:wght@400&display=swap">
<style>
  :root {
    --bg: #ececec;
    --card-white: #ffffff;
    --card-black: #1e1e1e;
    --ink: #1e1e1e;
    --ink-soft: #2a2a2a;
    --paper: #ffffff;
  }
  * { margin: 0; padding: 0; box-sizing: border-box; }
  html, body {
    width: 1200px; height: 967px; overflow: hidden;
    background: var(--bg);
  }
  .canvas {
    position: relative; width: 1200px; height: 967px;
  }
  .card {
    position: absolute; left: 232px; width: 736px; height: 420px;
    box-shadow: 0 6px 18px rgba(0,0,0,0.12);
  }
  .card--front { top: 52px; background: var(--card-white); color: var(--ink); }
  .card--back { top: 496px; background: var(--card-black); color: var(--paper); }

  .brand {
    position: absolute; display: flex; align-items: center; gap: 14px;
    font-family: "Montserrat", sans-serif; font-weight: 800;
    letter-spacing: 2px; text-transform: uppercase; white-space: nowrap;
  }
  .brand__mark { width: 22px; height: 22px; background: currentColor; }
  .card--front .brand { left: 300px; top: 84px; font-size: 50px; }
  .card--back .brand { left: 50%; top: 50%; transform: translate(-50%, -50%); font-size: 58px; }

  .person {
    position: absolute; left: 56px; top: 236px; width: 300px;
  }
  .person__name {
    font-family: "Montserrat", sans-serif; font-weight: 800;
    font-size: 30px; letter-spacing: 1px; text-transform: uppercase; line-height: 1.1;
  }
  .person__role {
    font-family: "Arimo", sans-serif; font-size: 17px; color: var(--ink-soft); margin-top: 4px;
  }
  .divider {
    position: absolute; left: 372px; top: 226px; width: 1.5px; height: 120px; background: var(--ink);
  }
  .contact {
    position: absolute; left: 396px; top: 236px; list-style: none;
    font-family: "Arimo", sans-serif; font-size: 19px; color: var(--ink-soft);
  }
  .contact__item { display: flex; align-items: center; gap: 10px; height: 32px; }
  .contact__icon { width: 15px; height: 15px; fill: var(--ink); flex: none; }
</style>
</head>
<body>
<main class="canvas">
  <section class="card card--front" aria-label="Business card front">
    <div class="brand"><span class="brand__mark"></span>RT Estates</div>
    <div class="person">
      <h1 class="person__name">Daniel Brooks</h1>
      <p class="person__role">Sales &amp; Property Management</p>
    </div>
    <div class="divider"></div>
    <ul class="contact">
      <li class="contact__item">
        <svg class="contact__icon" viewBox="0 0 16 16" aria-hidden="true"><path d="M3 1h3l1.5 4-2 1.2a9 9 0 0 0 4.3 4.3L11 8.5l4 1.5v3a2 2 0 0 1-2 2A12 12 0 0 1 1 3a2 2 0 0 1 2-2z"/></svg>
        0412583047
      </li>
      <li class="contact__item">
        <svg class="contact__icon" viewBox="0 0 16 16" aria-hidden="true"><path d="M1 3h14v1.2L8 9 1 4.2z"/><path d="M1 5.6 8 10.4l7-4.8V13H1z"/></svg>
        danielb@rtestates-demo.net.au
      </li>
      <li class="contact__item">
        <svg class="contact__icon" viewBox="0 0 16 16" aria-hidden="true"><circle cx="8" cy="8" r="7"/><path d="M1 8h14M8 1c-3 3.5-3 10.5 0 14M8 1c3 3.5 3 10.5 0 14" stroke="#fff" stroke-width="1" fill="none"/></svg>
        www.rtestates-demo.net.au
      </li>
    </ul>
  </section>

  <section class="card card--back" aria-label="Business card back">
    <div class="brand"><span class="brand__mark"></span>RT Estates</div>
  </section>
</main>
</body>
</html>
```